Stationary Package for Construction Company
Harborline Construction & Development, LLC
Stationary Package for Construction Company - Construction
Creative Brief
Bright & Fun-filled
Kevin R. Tolliver
Partner
1587 Marlow Avenue, STE 210 Myrtle Beach, SC 29577
kevin@harborlinehomebuilders.example
www.harborlinehomebuilders.example
travelkq travelkq

```html
<!DOCTYPE html>
<html lang="en">
<head>
<meta charset="utf-8">
<title>Harborline Construction &amp; Development – Business Cards</title>
<link href="https://fonts.googleapis.com/css2?family=Montserrat:wght@400;600;700&family=Open+Sans:wght@400;600&display=swap" rel="stylesheet">
<style>
  :root {
    --brand-red: #e8222b;
    --backdrop-red: #ea242b;
    --ink-black: #1b1b1b;
    --panel-gray: #3a3a3a;
    --text-gray: #4a4a4a;
    --paper: #ffffff;
  }
  * { margin: 0; padding: 0; box-sizing: border-box; }
  html, body { width: 1200px; height: 871px; overflow: hidden; }
  body { background: var(--backdrop-red); position: relative; font-family: "Open Sans", Arial, sans-serif; }

  .card {
    position: absolute; left: 312px; width: 576px; height: 355px;
    background: var(--paper); overflow: hidden;
    box-shadow: 6px 8px 14px rgba(0,0,0,0.28);
  }
  .card--front { top: 48px; }
  .card--back { top: 464px; }
  .card__art { position: absolute; inset: 0; }

  .front__mark { position: absolute; left: 42px; top: 96px; width: 106px; text-align: center; }
  .front__mark-name {
    display: block; margin-top: 10px; font-family: "Montserrat", sans-serif;
    font-weight: 700; font-size: 12px; letter-spacing: 1px; color: var(--brand-red);
  }

  .holder { position: absolute; left: 270px; top: 50px; font-family: "Montserrat", sans-serif; }
  .holder__name { font-size: 20px; font-weight: 400; color: var(--text-gray); letter-spacing: -0.2px; }
  .holder__name strong { color: var(--brand-red); font-weight: 700; }
  .holder__title { font-size: 17px; color: var(--text-gray); }

  .contact { position: absolute; left: 262px; top: 180px; width: 314px; height: 160px; background: var(--panel-gray); }
  .contact__row {
    position: relative; height: 26.6px; display: flex; align-items: center;
    padding-left: 44px; color: #fff; font-size: 10.5px; line-height: 1.1;
  }
  .contact__row:nth-child(odd)::before {
    content: ""; position: absolute; left: 30px; right: -10px; top: 2px; bottom: 2px;
    background: var(--ink-black); transform: skewX(-25deg);
  }
  .contact__row span { position: relative; }
  .contact__icon {
    position: absolute; left: 6px; top: 4px; width: 19px; height: 19px;
    background: var(--brand-red); border-radius: 3px 10px 10px 3px;
  }
  .contact__icon svg { width: 19px; height: 19px; display: block; }

  .back__logo { position: absolute; left: 242px; top: 150px; display: flex; align-items: center; gap: 12px; }
  .back__dot { width: 44px; height: 44px; border-radius: 50%; border: 4px solid var(--brand-red); flex: none; }
  .back__name { font-family: "Montserrat", sans-serif; font-weight: 600; font-size: 27px; letter-spacing: 2px; color: var(--ink-black); line-height: 1; }
  .back__tagline { font-family: "Montserrat", sans-serif; font-size: 8.5px; color: var(--brand-red); letter-spacing: 0.4px; margin-top: 6px; }
</style>
</head>
<body>

<section class="card card--front" aria-label="Business card front">
  <svg class="card__art" viewBox="0 0 576 355" aria-hidden="true">
    <rect x="0" y="0" width="190" height="30" fill="var(--brand-red)"/>
    <polygon points="0,235 214,235 177,355 0,355" fill="var(--brand-red)"/>
    <polygon points="177,0 197,0 252,177 197,355 177,355 232,177" fill="var(--brand-red)"/>
    <polyline points="207,0 262,177 207,355" fill="none" stroke="var(--ink-black)" stroke-width="4"/>
    <polyline points="219,0 274,177 219,355" fill="none" stroke="var(--brand-red)" stroke-width="3"/>
    <rect x="236" y="0" width="10" height="36" fill="var(--ink-black)" transform="skewX(17)"/>
  </svg>

  <div class="front__mark">
    <svg width="86" height="86" viewBox="0 0 86 86" aria-hidden="true"><circle cx="43" cy="43" r="39" fill="none" stroke="var(--brand-red)" stroke-width="5"/></svg>
    <span class="front__mark-name">HARBORLINE</span>
  </div>

  <div class="holder">
    <p class="holder__name"><strong>KEVIN R.</strong> TOLLIVER</p>
    <p class="holder__title">PARTNER</p>
  </div>

  <div class="contact">
    <div class="contact__row"><i class="contact__icon"><svg viewBox="0 0 19 19"><path d="M9.5 4a3.3 3.3 0 0 0-3.3 3.3c0 2.5 3.3 6.3 3.3 6.3s3.3-3.8 3.3-6.3A3.3 3.3 0 0 0 9.5 4zm0 4.6a1.3 1.3 0 1 1 0-2.6 1.3 1.3 0 0 1 0 2.6z" fill="#fff"/></svg></i><span>1587 Marlow Avenue, STE 210<br>Myrtle Beach, SC 29577</span></div>
    <div class="contact__row"><i class="contact__icon"><svg viewBox="0 0 19 19"><path d="M4 6h11v7H4z M4 6l5.5 4L15 6" fill="none" stroke="#fff" stroke-width="1.2"/></svg></i><span>kevin@harborlinehomebuilders.example</span></div>
    <div class="contact__row"><i class="contact__icon"><svg viewBox="0 0 19 19"><path d="M6 4.5l2 2.3-1.2 1.4a7 7 0 0 0 3.5 3.5l1.4-1.2 2.3 2-1.2 1.8C9 14 5 10 4.5 5.7z" fill="#fff"/></svg></i><span>PHONE: + 843.555.0142<br>843.555.0187</span></div>
    <div class="contact__row"><i class="contact__icon"><svg viewBox="0 0 19 19"><path d="M6 4.5l2 2.3-1.2 1.4a7 7 0 0 0 3.5 3.5l1.4-1.2 2.3 2-1.2 1.8C9 14 5 10 4.5 5.7z" fill="#fff"/></svg></i><span>866.555.0163</span></div>
    <div class="contact__row"><i class="contact__icon"><svg viewBox="0 0 19 19"><circle cx="9.5" cy="9.5" r="5" fill="none" stroke="#fff" stroke-width="1.2"/><path d="M4.5 9.5h10M9.5 4.5c-2.5 3-2.5 7 0 10M9.5 4.5c2.5 3 2.5 7 0 10" fill="none" stroke="#fff" stroke-width="1"/></svg></i><span>www.harborlinehomebuilders.example</span></div>
    <div class="contact__row"><span></span></div>
  </div>
</section>

<section class="card card--back" aria-label="Business card back">
  <svg class="card__art" viewBox="0 0 576 355" aria-hidden="true">
    <rect x="0" y="0" width="170" height="32" fill="var(--brand-red)"/>
    <polygon points="0,250 180,250 150,355 0,355" fill="var(--brand-red)"/>
    <polygon points="160,0 180,0 212,177 180,355 160,355 192,177" fill="var(--brand-red)"/>
    <polyline points="190,0 222,177 190,355" fill="none" stroke="var(--brand-red)" stroke-width="4"/>
    <polyline points="200,0 232,177 200,355" fill="none" stroke="var(--brand-red)" stroke-width="2"/>
  </svg>
  <div class="back__logo">
    <span class="back__dot"></span>
    <div>
      <p class="back__name">HARBORLINE</p>
      <p class="back__tagline">CONSTRUCTION AND DEVELOPMENT</p>
    </div>
  </div>
</section>

</body>
</html>
```